Email Signature

We are looking for creative email signature for our company. Please find attached the logo of our company for your reference. now we understand there isn't much can be done with email signature but we are looking for out of the box designs. Nothing specific in mind

Please insert fake numbers, website and/or address, etc just to showcase the designs. once the design is chosen we will provide the actual details.
Updates

Dear All,

We wouldlike to extend our apology for not being able to provide feedbacks to everysingle design. We were extremely busy and we have multiple contests opensimultaneously which makes the process harder. However, thank you all for theefforts you have put into this contest. We have received anoverwhelming quality responses & it has been a very difficult task tochoose just one, we easily Loved at least several designs...

Thanksagain for participating, we wish you all success in your design ventures.

Kindregards,

KLC Team

Industry/Entity Type

It Company

```html
<!DOCTYPE html>
<html lang="en">
<head>
<meta charset="utf-8">
<title>Kitchen Lantern Co – Email Signature</title>
<link href="https://fonts.googleapis.com/css2?family=Arimo:wght@400;700&display=swap" rel="stylesheet">
<style>
  :root {
    --paper: #ffffff;
    --ink: #111111;
    --accent-green: #72d72a;
    --brand-blue: #3b8fe4;
    --rule: #d5dde3;
  }
  html, body {
    margin: 0;
    padding: 0;
    overflow: hidden;
    background: var(--paper);
  }
  .signature-canvas {
    position: relative;
    width: 900px;
    height: 1200px;
    background: var(--paper);
    font-family: "Arimo", Arial, sans-serif;
    color: var(--ink);
    overflow: hidden;
  }
  .identity {
    position: absolute;
    left: 118px;
    top: 972px;
    line-height: 17px;
  }
  .identity-company, .identity-role {
    font-size: 14px;
    display: block;
  }
  .identity-name {
    font-size: 17px;
    font-weight: 700;
    display: block;
    line-height: 18px;
  }
  .brand-mark {
    position: absolute;
    right: 110px;
    top: 960px;
    display: flex;
    align-items: center;
    gap: 10px;
  }
  .brand-dot {
    width: 18px;
    height: 18px;
    border-radius: 50%;
    background: var(--accent-green);
  }
  .brand-name {
    font-size: 34px;
    font-weight: 700;
    color: var(--brand-blue);
    letter-spacing: -0.5px;
  }
  .divider {
    position: absolute;
    left: 118px;
    top: 1033px;
    width: 672px;
    height: 2px;
    background: var(--rule);
  }
  .contact-line {
    position: absolute;
    font-size: 14px;
    white-space: nowrap;
  }
  .contact-label { color: var(--accent-green); }
  .contact-phone  { left: 118px; top: 1048px; }
  .contact-mobile { left: 291px; top: 1048px; }
  .contact-email  { left: 458px; top: 1048px; }
  .contact-web    { left: 636px; top: 1048px; }
  .contact-address{ left: 118px; top: 1071px; }
</style>
</head>
<body>
<div class="signature-canvas">
  <div class="identity">
    <span class="identity-company">Nature of the company</span>
    <span class="identity-name">Marten L. Hove</span>
    <span class="identity-role">Designers</span>
  </div>

  <div class="brand-mark">
    <span class="brand-dot"></span>
    <span class="brand-name">Kitchen Lantern</span>
  </div>

  <div class="divider"></div>

  <div class="contact-line contact-phone"><span class="contact-label">Phone:</span>+22 410 55218</div>
  <div class="contact-line contact-mobile"><span class="contact-label">Mobil:</span>+35 702 14390</div>
  <div class="contact-line contact-email"><span class="contact-label">Email:</span>hello@lantern.dk</div>
  <div class="contact-line contact-web"><span class="contact-label">Web:</span>www.klantern.com</div>
  <div class="contact-line contact-address"><span class="contact-label">Address:</span>Instead of the address can be replaced</div>
</div>
</body>
</html>
```